Personal Training

The name of my company is Heron Fitness. I am looking for a design that will feature the 8 components I am utilizing in my workouts (strength, flexibility, agility, core, power, balance, cardiovacular, speed) and represent the spider. It is not essesstial to have a spider for my logo but would be nice. If a spider is used please do not use a logo like Gullwoman, a tarantula, or anything scary involving a spider (I have female clients who would get scared) lol
If you need me to provide more information please let me know. Feel free to check my website for ideas but ignore the pictures on my site as those are not pictures of me or clients
Thank you in advance!

Industry/Entity Type

Fitness

Contact Information for Business Card

Mark Delaney
Company Name: Heron Fitness
Tag line: 8 steps to a stronger you
Website: hernfit4.example
Email: mark@hernfit4.example
Cell: 555-314-2086

CQBL Certified Personal Trainer
CPR AED National Pulse Federation
B.A. Exercise Physiology W.K.R., 2004

```html
<!DOCTYPE html>
<html lang="en">
<head>
<meta charset="utf-8">
<title>Heron Fitness – Business Card</title>
<link rel="stylesheet" href="https://fonts.googleapis.com/css2?family=Open+Sans:wght@400;600;700&display=swap">
<style>
  :root {
    --page-bg: #e4e4e4;
    --card-black: #1b1b1b;
    --band-black: #0c0c0c;
    --card-white: #ffffff;
    --brand-yellow: #f2c417;
    --ink: #151515;
    --ink-soft: #333333;
    --text-font: "Open Sans", Arial, sans-serif;
  }
  * { box-sizing: border-box; margin: 0; padding: 0; }
  html, body {
    width: 1200px;
    height: 1000px;
    overflow: hidden;
    background: var(--page-bg);
    font-family: var(--text-font);
  }
  .sheet {
    width: 1200px;
    height: 1000px;
    display: flex;
    flex-direction: column;
    align-items: center;
    justify-content: center;
    gap: 60px;
  }
  .card {
    width: 700px;
    height: 400px;
    position: relative;
    overflow: hidden;
    box-shadow: 0 6px 18px rgba(0,0,0,0.18);
  }

  /* Front */
  .card-front {
    background: var(--card-black);
    border-top: 26px solid var(--band-black);
    border-bottom: 46px solid var(--band-black);
    display: flex;
    align-items: center;
    padding-left: 90px;
    gap: 40px;
  }
  .brand-dot {
    width: 150px;
    height: 150px;
    border-radius: 50%;
    flex: none;
  }
  .card-front .brand-dot { background: #ffffff; }
  .front-wordmark {
    color: var(--brand-yellow);
    font-weight: 400;
  }
  .front-wordmark .brand-name {
    font-size: 34px;
    line-height: 1.05;
    letter-spacing: 0.5px;
  }
  .front-wordmark .tagline {
    font-size: 16px;
    margin-top: 4px;
  }

  /* Back */
  .card-back {
    background: var(--card-white);
    border-top: 18px solid var(--band-black);
    border-bottom: 70px solid var(--band-black);
    display: flex;
    padding: 34px 40px 0 60px;
  }
  .back-brand {
    width: 280px;
    display: flex;
    flex-direction: column;
    align-items: center;
    justify-content: center;
    padding-bottom: 10px;
  }
  .card-back .brand-dot {
    width: 120px;
    height: 120px;
    background: var(--brand-yellow);
  }
  .back-brand .brand-name {
    margin-top: 26px;
    font-size: 26px;
    font-weight: 400;
    color: var(--ink);
    letter-spacing: 0.3px;
  }
  .contact-block {
    flex: 1;
    padding-left: 60px;
    color: var(--ink);
  }
  .person-name {
    font-size: 20px;
    font-weight: 700;
    letter-spacing: 0.5px;
  }
  .credentials {
    list-style: none;
    padding-left: 8px;
    font-size: 13.5px;
    line-height: 1.3;
    color: var(--ink-soft);
  }
  .credentials li.indent { padding-left: 10px; }
  .contact-table {
    margin-top: 20px;
    border-collapse: collapse;
    font-size: 14px;
  }
  .contact-table th {
    text-align: left;
    font-weight: 700;
    padding: 1px 10px 1px 0;
  }
  .contact-table td { padding: 1px 0; }
  .contact-table td.sep { padding-right: 8px; font-weight: 700; }
</style>
</head>
<body>
  <main class="sheet">
    <section class="card card-front" aria-label="Business card front">
      <div class="brand-dot"></div>
      <div class="front-wordmark">
        <div class="brand-name">HERON FITNESS</div>
        <div class="tagline">8 steps to a stronger you</div>
      </div>
    </section>

    <section class="card card-back" aria-label="Business card back">
      <div class="back-brand">
        <div class="brand-dot"></div>
        <div class="brand-name">HERON FITNESS</div>
      </div>
      <div class="contact-block">
        <h1 class="person-name">MARK DELANEY</h1>
        <ul class="credentials">
          <li>CQBL Certified Personal Trainer</li>
          <li class="indent">CPR</li>
          <li class="indent">AED</li>
          <li class="indent">National Pulse Federation</li>
          <li class="indent">B.A. Exercise</li>
          <li class="indent">Physiology W.K.R., 2004</li>
        </ul>
        <table class="contact-table">
          <tr><th>Cell</th><td class="sep">:</td><td>555-314-2086</td></tr>
          <tr><th>Email</th><td class="sep">:</td><td>mark@hernfit4.example</td></tr>
          <tr><th>Web</th><td class="sep">:</td><td>www.hernfit4.example</td></tr>
        </table>
      </div>
    </section>
  </main>
</body>
</html>
```